Bright Lantern Studios - Redesign of our website - needs to be dynamic and alive!

We provide fun lessons exclusively in students' homes in music, art, yoga and acting. I like most of the graphics and copy on the site now, but it looks too static and there might be too much info to read on the home page. Needs movement, needs to generate excitement and be a fun place to visit, yet keeping professional-looking. The site needs better SEO, a better look and needs to generate more business, as several people see it each day but few contact us for details about our program. The site is lantern-studios-example.com. I'd like it to continue to be hosted on my domain in Wordpress format so I can add and delete teacher photos from time to time. I like the way the teachers' bios currently pop up when a cursor is hovered over them on the Our Team page. Thank you and good luck!

Target Market(s)

Wealthy, college-educated households with children who live in the Greater Atlanta area

Industry/Entity Type

Education

Coding

Coded - Design and coding required

Number of Pages Required

5+ page

Requirements
Must have
• Home Page movement, excitement, but keeping it professional-looking. We're an educational company and want to market to people who are looking for a professional yet fun/exciting approach to lessons in their homes.
Nice to have
• The info on the Testimonials page can probably rotate and fade in/fade out on the home page or slide on/slide off instead of having a separate page for these.
• The info on the Trial Lessons page can probably be included as a banner on the home page too instead of being a separate page. Nice if I can change the text on this myself from time to time to mention any promotions I might be offering with regard to trial lessons.

```html
<!DOCTYPE html>
<html lang="en">
<head>
<meta charset="utf-8">
<title>Bright Lantern Studios – In-home Music, Art, Yoga & Acting Lessons</title>
<link href="https://fonts.googleapis.com/css2?family=Lilita+One&family=Open+Sans:wght@400;600;700&family=Roboto:wght@400;500;700&display=swap" rel="stylesheet">
<style>
:root{
  --orange:#f7a51c;
  --orange-deep:#f26a2a;
  --blue:#1db3e2;
  --green:#a2c83b;
  --purple:#5a2a88;
  --purple-dark:#4a1f73;
  --gold:#f39c12;
  --text:#555;
  --dark:#222;
  --light:#f4f4f4;
  --peach:#fdf3ee;
  --white:#fff;
}
*{margin:0;padding:0;box-sizing:border-box}
html,body{width:1200px;height:4138px;overflow:hidden}
body{position:relative;font-family:'Open Sans',sans-serif;color:var(--text);background:var(--white)}
.abs{position:absolute}
.display{font-family:'Lilita One',sans-serif;font-weight:400;text-transform:uppercase}
.ph{position:absolute}

/* header */
.top-stripe{left:0;top:0;width:1200px;height:5px;background:linear-gradient(90deg,var(--orange) 0 25%,var(--blue) 25% 50%,var(--green) 50% 75%,var(--purple) 75%)}
.brand{left:97px;top:40px;display:flex;align-items:center;gap:10px}
.brand-mark{width:30px;height:30px;border-radius:50%;background:var(--purple)}
.brand-name{font-family:'Lilita One',sans-serif;font-size:24px;color:var(--purple);line-height:1}
.phone{left:868px;top:30px;font-family:'Lilita One',sans-serif;font-size:20px;color:var(--orange)}
.social-dot{top:26px;width:34px;height:34px;border-radius:50%;background:var(--blue)}
.nav{left:312px;top:96px;display:flex;gap:30px;font-family:'Lilita One',sans-serif;font-size:13px;text-transform:uppercase;color:var(--dark)}
.nav .active{color:var(--orange)}

/* hero */
.hero{left:0;top:143px;width:1200px;height:519px;background:linear-gradient(120deg,#cfc6bb 0%,#8a7b6c 35%,#3b3330 60%,#a89a8c 100%)}
.hero-panel{left:97px;top:367px;width:427px;height:213px;background:rgba(30,30,30,.55)}
.hero-title{left:113px;top:378px;font-family:'Roboto',sans-serif;font-size:44px;color:var(--white)}
.hero-text{left:113px;top:434px;width:390px;font-family:'Roboto',sans-serif;font-size:17px;line-height:28px;color:var(--white)}
.btn{display:inline-block;font-family:'Roboto',sans-serif;color:var(--white);background:var(--orange-deep);text-align:center}
.hero-btn{left:113px;top:510px;width:152px;height:40px;line-height:40px;font-size:17px;border-radius:3px}
.hero-dots{left:476px;top:553px;display:flex;gap:8px}
.hero-dots i{width:7px;height:7px;border-radius:50%;background:#fff;opacity:.6}
.hero-dots i:first-child{opacity:1}
.hero-edge{left:0;top:652px}

/* section titles */
.sec-title{left:0;width:1200px;text-align:center;font-size:30px}
.sec-title .a{color:var(--purple)} .sec-title .b{color:var(--gold)}

/* courses */
.course{top:800px;width:235px;height:345px;border-radius:4px;overflow:hidden}
.course .photo{position:absolute;left:0;top:0;width:235px;height:152px}
.course .body{position:absolute;left:0;top:152px;width:235px;height:193px;text-align:center;color:var(--white)}
.course .icon{position:absolute;left:96px;top:-22px;width:44px;height:44px;border-radius:50%;border:3px solid #fff;display:flex;align-items:center;justify-content:center}
.course h3{margin-top:34px;font-family:'Roboto',sans-serif;font-weight:500;font-size:18px;text-transform:uppercase}
.course p{margin:6px 18px 0;font-size:10px;line-height:15px}
.course .more{display:inline-block;margin-top:12px;padding:4px 16px;border:2px solid #fff;border-radius:12px;font-size:9px;font-weight:700;text-transform:uppercase;color:var(--white)}
.c-music .body,.c-music .icon{background:var(--orange)}
.c-art .body,.c-art .icon{background:var(--blue)}
.c-yoga .body,.c-yoga .icon{background:var(--green)}
.c-acting .body,.c-acting .icon{background:var(--orange-deep)}

/* about band */
.band{left:0;top:1214px;width:1200px;height:419px;background:var(--light);border-top:3px solid #e2e2e2;border-bottom:3px solid #e2e2e2}
.band-left{left:40px;top:1250px;width:230px;height:383px;background:linear-gradient(160deg,#e8d3c6,#c8463e 70%,#8a3a2e)}
.band-right{left:950px;top:1250px;width:250px;height:383px;background:linear-gradient(200deg,#f3c7a4,#d8862a 50%,#c0392b)}
.band-title{left:250px;top:1280px;width:700px;text-align:center;font-size:27px;line-height:46px;color:var(--gold)}
.band-text{left:290px;top:1388px;width:620px;text-align:center;font-size:14px;line-height:24px;color:#666}
.band-btn{left:529px;top:1540px;width:142px;height:40px;line-height:40px;border-radius:20px;font-size:15px;text-transform:uppercase}

/* testimonials */
.t-ring{left:97px;top:1750px;width:160px;height:160px;border-radius:50%;background:var(--blue)}
.t-photo{left:165px;top:1758px;width:150px;height:150px;border-radius:50%;background:linear-gradient(160deg,#d9d2cc,#8b817a);border:4px solid #fff}
.t-quote{left:113px;top:1810px;font-family:Georgia,serif;font-size:60px;line-height:60px;color:var(--white)}
.t-mark{font-family:Georgia,serif;font-size:40px;color:var(--blue);line-height:1}
.t-text{left:370px;top:1778px;width:730px;font-size:14px;line-height:24px;color:#777}
.t-source{left:370px;top:1890px;font-size:15px;color:var(--blue)}
.t-dashes{left:521px;top:1963px;display:flex;gap:6px}
.t-dashes i{width:36px;height:4px;background:#ddd}
.t-dashes i.on{background:var(--blue)}

/* teachers */
.teachers{left:0;top:2033px;width:1200px;height:649px;background:radial-gradient(circle at 50% 55%,#6a35a0 0%,var(--purple) 45%,var(--purple-dark) 100%)}
.teachers-title{color:var(--white)}
.teacher{height:217px;display:flex}
.teacher .photo{width:207px;height:217px}
.teacher .bio{flex:1;padding:14px 18px;color:var(--white)}
.teacher h4{font-family:'Roboto',sans-serif;font-weight:500;font-size:17px;text-transform:uppercase}
.teacher .role{font-size:11px;margin:2px 0 8px}
.teacher p{font-size:9.5px;line-height:14px}
.teacher .link{display:block;margin-top:12px;font-size:11px}
.bio.green{background:var(--green)} .bio.blue{background:var(--blue)}

/* programs */
.programs{left:0;top:2682px;width:1200px;height:615px;background:var(--peach)}
.programs-girl{left:800px;top:2720px;width:400px;height:577px;background:linear-gradient(180deg,#f6d9c2 0%,#f08a22 60%,#e46d12 100%);border-radius:200px 0 0 0}
.prog-title{left:97px;top:2735px;font-size:30px}
.prog{left:97px;width:640px;display:flex;gap:22px}
.prog .ico{flex:none;width:72px;height:72px;border-radius:50%;display:flex;align-items:center;justify-content:center}
.prog h5{font-family:'Roboto',sans-serif;font-size:19px;font-weight:500;margin:6px 0 6px}
.prog p{font-size:13px;line-height:21px;color:#444}

/* cta */
.cta{left:0;top:3297px;width:1200px;height:295px;background:radial-gradient(circle at 50% 40%,#8ec63f,#5ea82f 80%)}
.cta-title{left:0;top:3355px;width:1200px;text-align:center;font-size:32px;line-height:52px;color:var(--white)}
.cta-btn{left:514px;top:3488px;width:172px;height:48px;line-height:48px;border-radius:24px;border:3px solid #fff;font-size:16px;text-transform:uppercase}

/* strip */
.strip{left:0;top:3592px;width:1200px;height:193px;background:linear-gradient(90deg,#2b2624 0%,#8d7c6b 18%,#3a302b 32%,#b9a794 50%,#4b3c33 66%,#9c8a78 82%,#2f2926 100%)}

/* footer */
.fcol{top:3840px;width:230px}
.fcol h6{font-family:'Roboto',sans-serif;font-size:16px;font-weight:500;color:var(--dark);text-transform:uppercase;margin-bottom:16px}
.fcol li{list-style:none;font-size:12px;color:#777;line-height:30px}
.fcol .nl{font-size:12px;line-height:20px;color:#777;margin-bottom:20px}
.fcol .input{width:282px;height:32px;border:1px solid #ddd;background:#f8f8f8;font-size:10px;color:#999;padding:9px 10px}
.fcol .sub{margin-top:10px;width:282px;height:34px;line-height:34px;background:var(--purple);border-radius:4px;font-size:13px;font-weight:700;text-transform:uppercase}
.copy-line{left:97px;top:4078px;width:1006px;height:1px;background:#e6e6e6}
.copy{left:97px;top:4095px;font-size:11px;color:#555}
.fsocial{left:948px;top:4090px;display:flex;gap:8px}
.fsocial i{width:22px;height:22px;border-radius:50%;border:1px solid #999}
</style>
</head>
<body>

<!-- Header -->
<div class="abs top-stripe"></div>
<div class="abs brand"><span class="brand-mark"></span><span class="brand-name">Bright Lantern Studios</span></div>
<div class="abs phone">(404) 555-0182</div>
<span class="abs social-dot" style="left:1029px"></span>
<span class="abs social-dot" style="left:1068px"></span>
<nav class="abs nav">
  <span class="active">Home</span><span>About Us</span><span>Courses</span><span>Programs</span><span>Our Team</span><span>Trial Lessons</span><span>Gallery</span><span>Testimonials</span><span>Contact</span>
</nav>

<!-- Hero -->
<div class="abs hero" role="img" aria-label="Photo of a student playing guitar beside a young drummer at a lesson"></div>
<div class="abs hero-panel"></div>
<h1 class="abs hero-title">Imagine</h1>
<p class="abs hero-text">Learning to play a musical instrument should be an enjoyable journey...</p>
<span class="abs btn hero-btn">Trial Lessons</span>
<div class="abs hero-dots"><i></i><i></i></div>
<svg class="abs hero-edge" width="1200" height="12" viewBox="0 0 1200 12"><path d="M0 12 L0 6 Q5 0 10 6 T20 6 T30 6 T40 6 T50 6 T60 6 T70 6 T80 6 T90 6 T100 6 T110 6 T120 6 T130 6 T140 6 T150 6 T160 6 T170 6 T180 6 T190 6 T200 6 T210 6 T220 6 T230 6 T240 6 T250 6 T260 6 T270 6 T280 6 T290 6 T300 6 T310 6 T320 6 T330 6 T340 6 T350 6 T360 6 T370 6 T380 6 T390 6 T400 6 T410 6 T420 6 T430 6 T440 6 T450 6 T460 6 T470 6 T480 6 T490 6 T500 6 T510 6 T520 6 T530 6 T540 6 T550 6 T560 6 T570 6 T580 6 T590 6 T600 6 T610 6 T620 6 T630 6 T640 6 T650 6 T660 6 T670 6 T680 6 T690 6 T700 6 T710 6 T720 6 T730 6 T740 6 T750 6 T760 6 T770 6 T780 6 T790 6 T800 6 T810 6 T820 6 T830 6 T840 6 T850 6 T860 6 T870 6 T880 6 T890 6 T900 6 T910 6 T920 6 T930 6 T940 6 T950 6 T960 6 T970 6 T980 6 T990 6 T1000 6 T1010 6 T1020 6 T1030 6 T1040 6 T1050 6 T1060 6 T1070 6 T1080 6 T1090 6 T1100 6 T1110 6 T1120 6 T1130 6 T1140 6 T1150 6 T1160 6 T1170 6 T1180 6 T1190 6 T1200 6 L1200 12 Z" fill="#fff"/></svg>

<!-- Courses -->
<h2 class="abs sec-title display" style="top:725px"><span class="a">Our </span><span class="b">Courses</span></h2>

<article class="abs course c-music" style="left:97px">
  <div class="photo" role="img" aria-label="Photo of a drum and keyboard lesson" style="background:linear-gradient(160deg,#6b5c52,#2a2522)"></div>
  <div class="body">
    <span class="icon"><svg width="20" height="20" viewBox="0 0 20 20"><path d="M7 15V4l9-2v11" stroke="#fff" stroke-width="2" fill="none"/><circle cx="5" cy="15" r="2.5" fill="#fff"/><circle cx="14" cy="13" r="2.5" fill="#fff"/></svg></span>
    <h3>Music Lessons</h3>
    <p>Nemo enim ipsam voluptatem quia voluptas sit aspernatur aut odit aut fugit, sed quia consequ.</p>
    <span class="more">Read More</span>
  </div>
</article>
<article class="abs course c-art" style="left:353px">
  <div class="photo" role="img" aria-label="Photo of children painting at an art lesson" style="background:linear-gradient(160deg,#e9d6c4,#b98d6a)"></div>
  <div class="body">
    <span class="icon"><svg width="20" height="20" viewBox="0 0 20 20"><circle cx="10" cy="10" r="7" stroke="#fff" stroke-width="2" fill="none"/><circle cx="7" cy="8" r="1.5" fill="#fff"/><circle cx="12" cy="7" r="1.5" fill="#fff"/><circle cx="13" cy="12" r="1.5" fill="#fff"/></svg></span>
    <h3>Art Lessons</h3>
    <p>Nemo enim ipsam voluptatem quia voluptas sit aspernatur aut odit aut fugit, sed quia consequ.</p>
    <span class="more">Read More</span>
  </div>
</article>
<article class="abs course c-yoga" style="left:610px">
  <div class="photo" role="img" aria-label="Photo of a young girl doing yoga outdoors" style="background:linear-gradient(160deg,#dfe8c8,#8fae5a)"></div>
  <div class="body">
    <span class="icon"><svg width="20" height="20" viewBox="0 0 20 20"><circle cx="10" cy="4" r="2" fill="#fff"/><path d="M3 9h14M10 7v6l-4 5M10 13l4 5" stroke="#fff" stroke-width="2" fill="none"/></svg></span>
    <h3>Yoga Classes</h3>
    <p>Nemo enim ipsam voluptatem quia voluptas sit aspernatur aut odit aut fugit, sed quia consequ.</p>
    <span class="more">Read More</span>
  </div>
</article>
<article class="abs course c-acting" style="left:866px">
  <div class="photo" role="img" aria-label="Photo of children acting in a park" style="background:linear-gradient(160deg,#c8d6a8,#5f8a3a)"></div>
  <div class="body">
    <span class="icon"><svg width="20" height="20" viewBox="0 0 20 20"><rect x="3" y="4" width="9" height="9" rx="3" fill="#fff"/><rect x="9" y="8" width="9" height="9" rx="3" fill="none" stroke="#fff" stroke-width="2"/></svg></span>
    <h3>Acting Lessons</h3>
    <p>Nemo enim ipsam voluptatem quia voluptas sit aspernatur aut odit aut fugit, sed quia consequ.</p>
    <span class="more">Read More</span>
  </div>
</article>

<!-- About band -->
<section class="abs band"></section>
<div class="abs band-left" role="img" aria-label="Photo of a smiling girl holding paintbrushes"></div>
<div class="abs band-right" role="img" aria-label="Photo of a boy playing an electric guitar"></div>
<h2 class="abs band-title display">Atlanta's Best Piano, Guitar, Voice, Art Lessons<br>and More, All Taught in Your Home.</h2>
<p class="abs band-text">Learning to play a musical instrument should be an enjoyable journey, not a chore. We exclusively offer in-home, individual music lessons for most instruments including piano, guitar, voice, drums, woodwinds, strings and many more using the unique Bright Lantern Studios Method. In addition to teaching the foundations of reading music we will help you play the styles of music and real songs you are excited to learn!</p>
<span class="abs btn band-btn">Read More</span>

<!-- Testimonials -->
<h2 class="abs sec-title display" style="top:1688px"><span class="a">Our </span><span class="b">Testimonials</span></h2>
<div class="abs t-ring"></div>
<div class="abs t-quote">&ldquo;</div>
<div class="abs t-photo" role="img" aria-label="Portrait photo of a parent reviewer"></div>
<span class="abs t-mark" style="left:348px;top:1772px">&ldquo;</span>
<p class="abs t-text">I can't say enough about how wonderful I think the Bright Lantern Studios program is. Our teacher makes learning a joy; I never have to ask my kids to practice. They have created a teaching method that enables every student to experience not just improved technique and knowledge, but enhanced pleasure in both making music and listening to it.</p>
<span class="abs t-mark" style="left:478px;top:1854px">&rdquo;</span>
<span class="abs t-source">Peachtree Reviews</span>
<div class="abs t-dashes"><i></i><i></i><i class="on"></i><i></i></div>

<!-- Teachers -->
<section class="abs teachers"></section>
<h2 class="abs sec-title display teachers-title" style="top:2078px">Meet Our Teachers</h2>

<article class="abs teacher" style="left:97px;top:2163px;width:477px">
  <div class="photo" role="img" aria-label="Portrait photo of the director" style="background:linear-gradient(160deg,#c9a58a,#6b4a38)"></div>
  <div class="bio green"><h4>Daniel's Bio – Director</h4><div class="role">Piano, Guitar, Voice, Saxophone</div>
    <p>Daniel has been teaching piano, guitar and voice since 1994, and is a founding member and Director of Bright Lantern Studios. He is a graduate of Ridgeview College, where his studies focused on music and child psychology.</p><span class="link">Read More &gt;&gt;</span></div>
</article>
<article class="abs teacher" style="left:607px;top:2163px;width:491px">
  <div class="photo" role="img" aria-label="Portrait photo of the piano teacher" style="background:linear-gradient(160deg,#d8d0c8,#5b4a40)"></div>
  <div class="bio blue"><h4>Priya's Bio</h4><div class="role">Piano</div>
    <p>Priya holds a J.D. from Northgate Law, a Bachelor's degree from Westbrook University, and has attained the highest level of certification through the state teachers' association Certificate of Merit piano program.</p><span class="link">Read More &gt;&gt;</span></div>
</article>
<article class="abs teacher" style="left:97px;top:2395px;width:477px">
  <div class="bio blue"><h4>Helena's Bio</h4><div class="role">Yoga (RYT-500)</div>
    <p>Helena is one of the original founders of Bright Lantern Studios, involved in its creation in 2002. She taught piano and dance for many years, and more recently has focused on studying and teaching yoga.</p><span class="link">Read More &gt;&gt;</span></div>
  <div class="photo" role="img" aria-label="Portrait photo of the yoga teacher" style="background:linear-gradient(160deg,#f0d7c4,#c4683a)"></div>
</article>
<article class="abs teacher" style="left:607px;top:2395px;width:491px">
  <div class="bio green"><h4>Claire's Bio</h4><div class="role">Voice, Piano</div>
    <p>Claire has been teaching voice and piano since 1994, and is a founding member of Bright Lantern Studios. She is a graduate of Ridgeview College, where her studies focused on music and child psychology.</p><span class="link">Read More &gt;&gt;</span></div>
  <div class="photo" role="img" aria-label="Portrait photo of the voice teacher" style="background:linear-gradient(160deg,#eee7e2,#8a5a40)"></div>
</article>

<!-- Programs -->
<section class="abs programs"></section>
<div class="abs programs-girl" role="img" aria-label="Photo of a girl singing into a microphone"></div>
<h2 class="abs prog-title display"><span style="color:var(--purple)">Our </span><span style="color:var(--gold)">Programs</span></h2>

<div class="abs prog" style="top:2828px">
  <span class="ico" style="background:var(--orange)"><svg width="30" height="30" viewBox="0 0 30 30"><rect x="4" y="7" width="22" height="19" rx="2" fill="none" stroke="#fff" stroke-width="2.5"/><path d="M4 13h22M10 3v7M20 3v7" stroke="#fff" stroke-width="2.5"/></svg></span>
  <div><h5 style="color:var(--orange)">Fall Spring Program:</h5><p>This is our primary program, consisting of 36 weekly lessons offered between September and May. Students who would like to begin after the first week.</p></div>
</div>
<div class="abs prog" style="top:2935px">
  <span class="ico" style="background:var(--green)"><svg width="30" height="30" viewBox="0 0 30 30"><path d="M6 24L24 6M6 6l18 18" stroke="#fff" stroke-width="3" stroke-linecap="round"/></svg></span>
  <div><h5 style="color:var(--green)">10-Session Workshops:</h5><p>All workshops in Theater, Music, Visual Arts and Yoga are offered in 10-Session packages which are renewable upon completion.</p></div>
</div>
<div class="abs prog" style="top:3035px">
  <span class="ico" style="background:var(--blue)"><svg width="30" height="30" viewBox="0 0 30 30"><circle cx="15" cy="15" r="6" fill="#fff"/><path d="M15 2v5M15 23v5M2 15h5M23 15h5M6 6l3 3M21 21l3 3M24 6l-3 3M9 21l-3 3" stroke="#fff" stroke-width="2.5"/></svg></span>
  <div><h5 style="color:var(--blue)">Summer Session:</h5><p>Summer's a great time to try lessons in a new subject or to continue work on progress that's occurred during the previous season.</p></div>
</div>
<div class="abs prog" style="top:3137px">
  <span class="ico" style="background:var(--purple)"><svg width="30" height="30" viewBox="0 0 30 30"><path d="M15 3l3.5 8 8.5.7-6.5 5.6 2 8.4L15 21l-7.5 4.7 2-8.4L3 11.7l8.5-.7z" fill="#fff"/></svg></span>
  <div><h5 style="color:var(--purple)">Trial Lessons:</h5><p>The first two lessons taught are considered "trial" lessons, helping you to determine if our program and the instructor we've offered are exactly right for your needs.</p></div>
</div>

<!-- Call to action -->
<section class="abs cta"></section>
<h2 class="abs cta-title display">Get Started a Trial Lessons<br>Today</h2>
<span class="abs btn cta-btn">Read More</span>

<!-- Photo strip -->
<div class="abs strip" role="img" aria-label="Row of photos from piano, drum, band and keyboard lessons"></div>

<!-- Footer -->
<div class="abs fcol" style="left:99px"><h6>About Us</h6><ul><li>About us</li><li>Shopping Guide</li><li>Delivery Information</li><li>Privacy Policy</li><li>Sitemap</li></ul></div>
<div class="abs fcol" style="left:353px"><h6>Courses</h6><ul><li>Music Lessons</li><li>Music Workshops</li><li>Acting Lessons</li><li>Visual Art Lessons</li><li>Yoga Classes</li></ul></div>
<div class="abs fcol" style="left:593px"><h6>Our Programs</h6><ul><li>Fall/Spring Program</li><li>10-Session Workshops</li><li>Summer Session</li><li>Trial Lessons</li></ul></div>
<div class="abs fcol" style="left:841px"><h6>Newsletter</h6><p class="nl">lorem ipsum dolor sit amet consectetur adipiscing elit</p><div class="input">Enter Your email</div><div class="btn sub">Subscribe Now</div></div>
<div class="abs copy-line"></div>
<p class="abs copy">Copyright © 2017 Bright Lantern Studios. All Rights Reserved</p>
<div class="abs fsocial"><i></i><i></i><i></i><i></i><i></i></div>

</body>
</html>
```